Flyer design 3-part folding flyer

A template for a 3-fold print flyer is to be created.

The flyer should be professional and customer-oriented as an advertising flyer that leads to the purchase of the consulting service.

The structure is an example and can be customized.
The topics are as follows:
Create a 3-part folded flyer:
🧠 Flyer design: KRVO Business Partner GmbH
🎨 Color scheme
Orange: Energy, innovation, attention
White: Clarity, trust
Anthracite: seriousness, stability

πŸ”Ά Front (Panel 1 – Title Page)
Title: From Chaos to Clarity – AI in Your Supply Chain
Image idea: An entrepreneur with a desperate look in front of a mountain of documents and storage chaos (horror of horrors) – next to it a signpost towards the β€œBeach of Bliss” with the logo of KRVO Business Partner GmbH.
Slogan: KRVO gets your supply chain on track – with artificial intelligence.

πŸ”Ά Inside (Panel 2 – Problem & Solution)
Headline: The challenges of modern supply chains
Key points (problem):
Overcrowded warehouses & capital tie-up
Unclear demand planning
Supply bottlenecks & production stoppages
Intransparent material flow
Errors that are detected too late
Headline Solution: Our AI solutions – your competitive advantages
Key points (solution):
βœ… Inventory reduction through intelligent forecasts
βœ… Optimized planning with real-time data
βœ… Delivery security through smart algorithms
βœ… Material flow optimization with AI
βœ… Real-time error detection and resolution

πŸ”Ά Back (Panel 3 – Call to Action & Contact)
Headline: Your path to the beach of bliss begins here.
Text: Say goodbye to the horror of horror in your supply chain.
KRVO Business Partner GmbH: Experience meets AI – we transform your supply chain from chaos to success. Fast. Precise. Powerful in implementation. πŸš€

Call to Action: πŸ“ž Get a non-binding consultation now +49 151 27406193 🌐 www.krvo-beratung.de βœ‰οΈ tobias.werndl@krvo-beratung.de πŸ“ Location: KRVO Business Partner GmbH, Hollenfelder Gasse 8, D-96251 Wiesmannsdorf

Logo & Design: KRVO logo positioned at the bottom right, with an orange, white, and anthracite frame and clear typography.

------------------------
If you have any questions or concerns, please contact me.

```html
<!DOCTYPE html>
<html lang="de">
<head>
<meta charset="utf-8">
<title>KRVO Business Partner – Faltflyer</title>
<link href="https://fonts.googleapis.com/css2?family=Poppins:wght@400;500;600;700;800&family=Great+Vibes&display=swap" rel="stylesheet">
<style>
:root{
  --orange:#f7941d;
  --anthracite:#3b4a4c;
  --ink:#2b2b2b;
  --white:#ffffff;
  --stage:#8f8f8f;
  --rule:#c9c9c9;
}
*{margin:0;padding:0;box-sizing:border-box}
html,body{width:791px;height:1200px;overflow:hidden}
body{background:var(--stage);font-family:'Poppins',sans-serif;color:var(--ink);position:relative}
.spread{position:absolute;left:74px;width:643px;height:497px;background:var(--white);overflow:hidden;box-shadow:6px 8px 10px rgba(0,0,0,.35)}
.spread.outside{top:81px}
.spread.inside{top:622px}
.shapes{position:absolute;left:0;top:0;width:643px;height:497px}
.abs{position:absolute}
.orange{color:var(--orange)}
.light{color:var(--white)}
.h-block{font-weight:800;line-height:1;text-transform:uppercase}
.script{font-family:'Great Vibes',cursive}
.small{font-size:6.4px;line-height:1.3}

/* brand name */
.brand-name{position:absolute;left:470px;top:22px;width:124px;text-align:right;font-size:36px;font-weight:500;line-height:1;color:var(--anthracite);letter-spacing:.5px}

/* problem / solution lists */
.tag{position:absolute;left:19px;width:100px;height:12px;border-radius:0 6px 6px 0;color:var(--white);font-size:7.5px;font-weight:700;letter-spacing:2px;padding-left:6px;line-height:12px}
.tag.dark{background:var(--anthracite)}
.tag.warm{background:var(--orange)}
.list{position:absolute;left:19px;width:170px;list-style:none}
.list li{display:flex;align-items:center;gap:5px;font-size:6.6px;line-height:1.2;height:20px}
.list li span.txt{flex:1;border-bottom:0.6px solid var(--rule);padding:3px 0}
.hex{width:16px;height:17px;flex:none;clip-path:polygon(50% 0,100% 25%,100% 75%,50% 100%,0 75%,0 25%);display:flex;align-items:center;justify-content:center}
.hex.dark{background:var(--anthracite)}
.hex.warm{background:var(--orange)}
.hex i{width:6px;height:6px;border:1.2px solid var(--white);border-radius:50%}

.pill{display:inline-block;font-size:6.4px;font-weight:600;border:1px solid var(--white);border-radius:8px;padding:1px 11px;color:var(--white)}
.pill.on{background:var(--orange);border-color:var(--orange)}
.contact-ico{display:inline-block;width:10px;height:10px;border-radius:50%;background:var(--orange);margin:0 1px}

.checks{list-style:none;position:absolute;left:19px;width:175px}
.checks li{font-size:6.2px;line-height:1.2;padding-left:10px;position:relative;margin-bottom:6px}
.checks li::before{content:"";position:absolute;left:0;top:1px;width:6px;height:6px;border-radius:50%;background:var(--anthracite)}
.checks li::after{content:"";position:absolute;left:1.6px;top:2.4px;width:2.4px;height:1.4px;border-left:1px solid #fff;border-bottom:1px solid #fff;transform:rotate(-45deg)}

.step{position:absolute;left:233px;display:flex;gap:8px;align-items:flex-start}
.step .num{width:22px;height:24px;background:var(--orange);clip-path:polygon(50% 0,100% 25%,100% 75%,50% 100%,0 75%,0 25%);color:#fff;font-weight:700;font-size:9px;display:flex;align-items:center;justify-content:center;flex:none}
.step h4{color:var(--orange);font-size:8.5px;font-weight:700;line-height:1.2}
.step p{color:#e8e8e8;font-size:6.8px;line-height:1.25;margin-top:2px}
.service{position:absolute;left:233px;display:flex;align-items:center;gap:8px;color:#fff;font-size:7px;font-weight:500}
.service .hex{width:24px;height:26px}
</style>
</head>
<body>

<!-- OUTSIDE SPREAD -->
<section class="spread outside">
  <svg class="shapes" viewBox="0 0 643 497">
    <polygon points="0,0 214,0 214,177 0,112" fill="#d9dde0" role="img" aria-label="Foto: Berater mit Tablet vor digitaler Benutzeroberfläche"/>
    <polygon points="214,30 408,60 570,110 643,88 643,252 428,290 428,497 214,497" fill="var(--anthracite)"/>
    <polygon points="214,165 428,243 428,258 214,180" fill="#ffffff"/>
    <polygon points="383,58 408,56 408,74" fill="var(--orange)"/>
    <polygon points="428,120 643,120 643,252 428,290" fill="#56686a" role="img" aria-label="Bild: verzweifelter Unternehmer vor einem einstürzenden Stapel Ordner mit Wanduhr"/>
    <polygon points="572,276 643,258 643,270 584,290" fill="var(--orange)"/>
    <polygon points="273,183 325,160 325,176 285,194 285,253 273,246" fill="var(--orange)"/>
    <polygon points="325,173 379,204 379,266 325,297 271,266 271,204" fill="#ffffff"/>
    <rect x="302" y="186" width="46" height="90" rx="3" fill="#4a3a30" role="img" aria-label="Bild: Kreidetafel-Aufsteller mit Wegweiser zum Strand der Glückseligkeit"/>
  </svg>

  <!-- panel: problem & solution -->
  <div class="abs h-block orange" style="left:19px;top:150px;font-size:15px">Problem</div>
  <div class="abs h-block" style="left:19px;top:166px;font-size:15px;color:var(--anthracite)">&amp; Lösung</div>
  <div class="abs" style="left:19px;top:195px;border-left:1.5px solid var(--ink);padding-left:5px;font-size:9px;font-weight:700;line-height:1.2">Die Herausforderungen<br>moderner Lieferketten</div>
  <div class="tag dark" style="top:229px">PROBLEM</div>
  <ul class="list" style="top:249px">
    <li><b class="hex dark"><i></i></b><span class="txt">Überfüllte Lager und Kapitalbindung</span></li>
    <li><b class="hex warm"><i></i></b><span class="txt">Unklare Bedarfsplanung</span></li>
    <li><b class="hex dark"><i></i></b><span class="txt">Lieferengpässe und Produktionsausfälle</span></li>
    <li><b class="hex warm"><i></i></b><span class="txt">Intransparenter Materialfluss</span></li>
    <li><b class="hex dark"><i></i></b><span class="txt">Fehler, die zu spät erkannt werden</span></li>
  </ul>
  <div class="tag warm" style="top:361px">SOLUTION</div>
  <ul class="list" style="top:380px">
    <li><b class="hex dark"><i></i></b><span class="txt">Bestandsreduzierung durch intelligente Prognosen</span></li>
    <li><b class="hex warm"><i></i></b><span class="txt">Optimierte Planung mit Echtzeitdaten</span></li>
    <li><b class="hex dark"><i></i></b><span class="txt">Liefersicherheit durch smarte Algorithmen</span></li>
    <li><b class="hex warm"><i></i></b><span class="txt">Materialflussoptimierung mit KI</span></li>
    <li><b class="hex dark"><i></i></b><span class="txt">Fehlererkennung und -behebung in Echtzeit</span></li>
  </ul>

  <!-- panel: call to action -->
  <div class="abs" style="left:214px;width:214px;text-align:center;top:82px">
    <div class="light" style="font-size:7.5px;font-weight:800;letter-spacing:2px">IHR WEG ZUM</div>
    <div class="orange" style="font-size:10.5px;font-weight:800;letter-spacing:.2px">STRAND DER GLÜCKSELIGKEIT</div>
    <div class="script light" style="font-size:19px;line-height:1.1">Beginnt Hier</div>
    <div class="light" style="font-size:7px;line-height:1.25;margin-top:2px">Verabschieden Sie sich vom Horror des<br>Horrors in Ihrer Lieferkette</div>
  </div>
  <div class="abs" style="left:214px;width:214px;text-align:center;top:309px">
    <div class="orange" style="font-size:7px;font-weight:700">KRVO Business Partner GmbH</div>
    <div class="light" style="font-size:6.2px;line-height:1.3">Erfahrung trifft KI – wir transformieren Ihre<br>Lieferkette vom Chaos zur</div>
    <div style="margin-top:5px"><span class="pill">Erfolg</span><span class="pill on">Schnell</span><span class="pill">Präzise</span></div>
    <div class="light" style="font-size:6.4px;margin-top:6px">Leistungsstarken Umsetzung</div>
    <div class="script light" style="font-size:15px;margin-top:8px">Jetzt unverbindlich beraten lassen</div>
    <div style="margin-top:4px"><span class="contact-ico"></span><span class="contact-ico"></span><span class="contact-ico"></span><span class="contact-ico"></span></div>
    <div class="light" style="font-size:6.4px;line-height:1.75;margin-top:4px">+49 151 27406193<br>www.krvo-beratung.de<br>tobias.werndl@krvo-beratung.de</div>
    <div class="light" style="font-size:6.2px;line-height:1.3">KRVO Business Partner GmbH,<br>Hollenfelder Gasse 8, D-96251 Wiesmannsdorf</div>
  </div>

  <!-- panel: title -->
  <div class="brand-name">KRVO</div>
  <div class="abs h-block" style="left:457px;top:295px;font-size:18px;color:var(--ink)">Vom</div>
  <div class="abs h-block orange" style="left:455px;top:312px;font-size:39px">Chaos</div>
  <div class="abs" style="left:458px;top:351px;font-size:20px;line-height:1;color:var(--ink)"><span style="font-weight:400">ZUR</span> <b style="font-weight:800">KLARHEIT</b></div>
  <div class="abs" style="left:461px;top:380px;width:152px;height:16px;border-radius:8px;background:var(--anthracite);color:#fff;font-size:8.5px;font-weight:700;text-align:center;line-height:16px">KI IN <span class="orange">IHRER LIEFERKETTE</span></div>
  <div class="abs" style="left:440px;width:190px;top:406px;text-align:center;font-size:9px;line-height:1.2">KRVO bringt Ihre Lieferkette auf Kurs – <b>mit künstlicher Intelligenz</b></div>
  <div class="abs" style="left:440px;width:190px;top:465px;text-align:center;font-size:8.5px;letter-spacing:1.2px">www.<b class="orange">krvo-beratung</b>.de</div>
</section>

<!-- INSIDE SPREAD -->
<section class="spread inside">
  <svg class="shapes" viewBox="0 0 643 497">
    <polygon points="0,0 214,0 214,177 0,112" fill="#c9d6e2" role="img" aria-label="Bild: Roboterhand berührt eine digitale Datenoberfläche"/>
    <polygon points="0,113 147,166 147,175 0,124" fill="var(--orange)"/>
    <polygon points="216,15 425,84 643,115 643,265 428,300 428,497 216,497" fill="var(--anthracite)"/>
    <polygon points="425,122 570,122 570,290 425,300" fill="#556567" role="img" aria-label="Foto: Porträt des Geschäftsführers im Anzug"/>
    <polygon points="570,278 643,265 643,278 582,294" fill="var(--orange)"/>
    <line x1="233" y1="176" x2="409" y2="176" stroke="#fff" stroke-width=".7"/>
    <line x1="233" y1="288" x2="409" y2="288" stroke="#fff" stroke-width=".7"/>
  </svg>

  <!-- panel: what we do -->
  <div class="abs h-block" style="left:19px;top:176px;font-size:12px"><span class="orange">Was</span> wir tun?</div>
  <p class="abs small" style="left:19px;top:194px;width:175px">Von der ersten Bestandsaufnahme bis zur passgenauen Umsetzung machen wir Ihre Lieferkette fit für alle Anforderungen, die Ihre Produktion, Ihre Produkte und Ihre Kunden an Sie stellen.</p>
  <div class="abs h-block" style="left:19px;top:251px;font-size:12px"><span class="orange">Das</span> Ziel?</div>
  <p class="abs small" style="left:19px;top:269px;width:170px">Reibungslose Versorgung Ihrer Produktion und maximale Kostensenkung entlang Ihrer gesamten Lieferkette!</p>
  <div class="abs h-block orange" style="left:19px;top:324px;font-size:12px">Konkret?</div>
  <ul class="checks" style="top:350px">
    <li>Kurzfristige Übernahme der Leitung Ihrer Supply-Chain bei unvorhergesehenen Ausfällen</li>
    <li>Zuverlässiges Lieferkettenmanagement und Win-win-Lieferantenbeziehungen</li>
    <li>Kosteneffiziente Lagerhaltung und „atmendes“ Bestandsmanagement</li>
    <li>Sichere Produktionsplanung und -steuerung</li>
    <li>Kosteneffiziente Lagerhaltung und „atmendes“ Bestandsmanagement</li>
    <li>Strukturierte Verlagerung und Neuausrichtung von Produktionsprozessen nach Plan</li>
  </ul>

  <!-- panel: services -->
  <div class="abs h-block light" style="left:233px;top:73px;font-size:12.5px"><span class="orange">Unsere</span> Leistungen</div>
  <div class="service" style="top:97px"><span class="hex" style="background:#fff;padding:1.2px"><span class="hex dark" style="width:100%;height:100%"><i></i></span></span>Ineffizienzen bei der Identifizierung</div>
  <div class="service" style="top:131px"><span class="hex warm"><i></i></span>Präzise Bestandsanalysen</div>
  <div class="abs h-block" style="left:233px;top:193px;font-size:12.5px;line-height:1.1"><span class="orange">Ihre Lieferkette</span><br><span class="light">auf dem Prüfstand?</span></div>
  <p class="abs light" style="left:233px;top:236px;width:135px;font-size:7px;line-height:1.25">KRVO prüft Ihre gesamte Wertschöpfungskette, deckt versteckte Kostentreiber auf und zeigt konkrete Potenziale für schnelle Verbesserungen.</p>
  <div class="abs h-block light" style="left:233px;top:314px;font-size:12.5px"><span class="orange">Wie wir</span> Vorgehen</div>
  <div class="step" style="top:340px"><span class="num">1</span><div><h4>Analyse</h4><p>Wir erfassen Ihre Prozesse<br>und Daten vor Ort</p></div></div>
  <div class="step" style="top:385px"><span class="num">2</span><div><h4>Empfehlungen</h4><p>Klare Maßnahmen, priorisiert<br>nach Wirkung und Aufwand<br>für Ihr Team.</p></div></div>
  <div class="step" style="top:438px"><span class="num">3</span><div><h4>Implementieren</h4><p>Gemeinsame Umsetzung mit KI</p></div></div>

  <!-- panel: why us -->
  <div class="abs h-block" style="left:448px;top:17px;font-size:12.5px"><span class="orange">Warum</span> wir?</div>
  <p class="abs small" style="left:448px;top:41px;width:180px">Ich bin Tobias Werndl. Und mein Herz schlägt seit 30 Jahren für die Supply-Chain. Hier passiert Verschwendung. Oder eben nicht.</p>
  <div class="abs light" style="left:544px;top:174px;line-height:1"><div style="font-size:18px;font-weight:800">TOBIAS</div><div style="font-size:17px;font-weight:400">WERNDL</div></div>
  <div class="abs" style="left:547px;top:213px;width:76px;height:12px;border-radius:6px;background:var(--orange);border:1px solid #fff;color:#fff;font-size:5px;font-weight:700;text-align:center;line-height:10px">MAKE AN APPOINTMENT</div>
  <div class="abs" style="left:447px;top:303px;width:180px;font-size:6px;line-height:1.3">
    <p>Diese Jagd nach<br>Verschwendung ist mein<br>Steckenpferd. Zu Beginn im<br>Speditionsumfeld, später in der<br>Automobilbranche und im Anlagenbau.</p>
    <p style="margin-top:7px">In knapp 20 Jahren in Führungspositionen – darunter bei Trelmo mit Verantwortung für 11 Werke und 220 Mitarbeiter – habe ich erlebt, was es heißt, aus einer komplexen Kette eine kraftvolle Einheit zu formen. Und die unzähligen Stellhebel für eine stabile Produktion, robuste Lieferketten und dauerhafte Kostensenkung perfekt zu synchronisieren.</p>
    <p style="margin-top:7px">Dieses Wissen gebe ich heute an meine Kunden weiter. Und um noch schlagkräftiger zu sein, habe ich deshalb vor 6 Jahren die KRVO Business Partner GmbH gegründet.</p>
    <p style="margin-top:7px;font-weight:700">Heute vertrauen uns Unternehmen wie Haverkamp, das Motorenwerk Lindt, Ostermaier, Veltron, Kessler Thermo, Nordmolkerei oder Carevita, wenn es in der Supply-Chain brennt oder notwendige Veränderungen umgesetzt werden müssen.</p>
  </div>
</section>

</body>
</html>
```